International Business Consulting Company Website

RV Crestline Advisory is a U.S-based international consulting firm. We combined passion for success in the global business arena with hands-on experience to help foreign companies navigate the entry into U.S. markets and U.S. companies in initiating and expanding exports to foreign markets.

We need a simple 1 page website
Examples of other consultants’ websites:
http://www.falconridgeadvisors.example/#intro
https://www.mtq-advisers.example
http://veronagroup.example
https://harborwiseadvisory.example

I also need the designer to suggest stock images that are suitable (related to international business, exports).

We want our web design to be bold, yet clean and simple.

Target Market(s)

US companies that export abroad, foreign companies that want to do business int he US/ open a subsidiary in the US.

Industry/Entity Type

Business Consultant

Coding

Coded - Design and coding required

Font styles to use
Sans Serif

Requirements
Must have
• Company logo on top

```html
<!DOCTYPE html>
<html lang="en">
<head>
<meta charset="utf-8">
<title>RV Crestline Advisory</title>
<link href="https://fonts.googleapis.com/css2?family=Lato:wght@300;400;700&family=Ubuntu:wght@300;400;500;700&display=swap" rel="stylesheet">
<style>
:root{
  --blue:#174a9c;
  --blue-dark:#123f88;
  --ink:#1f1f1f;
  --grey:#777777;
  --soft:#f7f7f7;
  --white:#ffffff;
  --orange:#f08a24;
  --orange-ring:#fbd3ad;
}
*{margin:0;padding:0;box-sizing:border-box}
html,body{width:1200px;height:1200px;overflow:hidden;background:var(--soft)}
body{font-family:'Lato',sans-serif;color:var(--ink);position:relative}

/* top bar */
.topbar{position:absolute;top:0;left:0;width:1200px;height:36px;background:var(--blue);color:var(--white);font-size:11px}
.topbar .contact{position:absolute;left:131px;top:0;height:36px;display:flex;align-items:center;gap:12px}
.topbar .sep{width:1px;height:12px;background:rgba(255,255,255,.4)}
.topbar .item{display:flex;align-items:center;gap:6px}
.topbar .right{position:absolute;right:131px;top:0;height:36px;display:flex;align-items:center;gap:12px}
.social{display:flex;gap:10px}
.social span{width:8px;height:8px;border-radius:50%;background:var(--white);display:block}
.quote{background:var(--blue-dark);height:36px;padding:0 13px;display:flex;align-items:center;font-family:'Ubuntu',sans-serif;font-weight:500;font-size:11px;letter-spacing:.5px}

/* header */
.header{position:absolute;top:36px;left:0;width:1200px;height:73px;background:var(--white);border-bottom:1px solid #e4e4e4}
.brand{position:absolute;left:131px;top:17px;display:flex;align-items:center;gap:8px}
.brand .mark{width:40px;height:40px;border:2px solid var(--blue)}
.brand .name{font-family:'Lato',sans-serif;font-weight:700;color:var(--blue);font-size:15px;letter-spacing:1px;line-height:1.1;width:120px}
.nav{position:absolute;left:374px;top:0;height:73px;display:flex;align-items:center;font-family:'Lato',sans-serif;font-size:12px;font-weight:400;color:#222}
.nav a{color:inherit;text-decoration:none;margin-right:42px}
.nav a:nth-child(3){margin-right:41px}
.search{position:absolute;left:1024px;top:13px;width:44px;height:44px;border-radius:50%;background:var(--orange-ring);display:flex;align-items:center;justify-content:center}
.search span{width:30px;height:30px;border-radius:50%;background:var(--orange);display:flex;align-items:center;justify-content:center}

/* hero */
.hero{position:absolute;top:109px;left:0;width:1200px;height:443px;overflow:hidden}
.hero-photo{position:absolute;inset:0;background:linear-gradient(90deg,#eaf1f7 0%,#dbe7f2 35%,#8fb5dc 60%,#6f9fd2 80%,#b7c9dc 100%)}
.hero-copy{position:absolute;left:131px;top:111px}
.hero h1{font-family:'Ubuntu',sans-serif;font-weight:300;font-size:35px;color:#111;line-height:1}
.hero h2{font-family:'Ubuntu',sans-serif;font-weight:700;font-size:50px;color:var(--blue);line-height:1;margin-top:10px;letter-spacing:.5px}
.hero p{font-size:13px;line-height:20px;color:#222;width:400px;margin-top:11px}
.btns{display:flex;gap:13px;margin-top:20px}
.btn{height:40px;display:flex;align-items:center;justify-content:center;font-size:12px;font-weight:700;font-family:'Lato',sans-serif}
.btn.solid{width:115px;background:var(--blue);color:var(--white)}
.btn.line{width:115px;border:2px solid var(--blue);color:var(--blue);background:var(--white)}

/* services */
.services-title{position:absolute;top:604px;left:0;width:1200px;text-align:center;font-family:'Ubuntu',sans-serif;font-weight:500;font-size:27px;color:#222;letter-spacing:.5px}
.rule{position:absolute;top:641px;left:555px;width:90px;height:4px;border-top:1px solid #333;border-bottom:1px solid #333}
.services-lead{position:absolute;top:660px;left:300px;width:600px;text-align:center;font-size:11px;line-height:18.5px;color:var(--grey);font-weight:400}
.card{position:absolute;width:295px;height:228px;background:var(--white);border-bottom:2px solid var(--blue);text-align:center;box-shadow:0 1px 4px rgba(0,0,0,.05)}
.card svg{position:absolute;left:50%;top:31px;transform:translateX(-50%)}
.card h3{position:absolute;top:100px;left:0;width:100%;font-family:'Ubuntu',sans-serif;font-weight:400;font-size:13px;letter-spacing:.6px;color:#111}
.card p{position:absolute;top:126px;left:30px;right:30px;font-size:11px;line-height:19px;color:var(--grey);font-weight:400}
.card .more{position:absolute;top:184px;left:0;width:100%;font-size:10.5px;color:var(--grey);letter-spacing:.3px}
.c1{left:133px}.c2{left:454px}.c3{left:773px}
.r1{top:738px}.r2{top:1000px}
</style>
</head>
<body>

<div class="topbar">
  <div class="contact">
    <div class="item"><svg width="10" height="10" viewBox="0 0 24 24"><path fill="#fff" d="M6.6 10.8a15 15 0 0 0 6.6 6.6l2.2-2.2c.3-.3.7-.4 1-.2 1.1.4 2.3.6 3.6.6.6 0 1 .4 1 1V20c0 .6-.4 1-1 1A17 17 0 0 1 3 4c0-.6.4-1 1-1h3.5c.6 0 1 .4 1 1 0 1.3.2 2.5.6 3.6.1.3 0 .7-.2 1z"/></svg>T +1 (555) 014-2290</div>
    <div class="sep"></div>
    <div class="item"><svg width="10" height="8" viewBox="0 0 20 14"><rect x="0" y="0" width="20" height="14" fill="#fff"/><path d="M0 0l10 8 10-8" fill="none" stroke="#174a9c" stroke-width="1.5"/></svg>hello@rvcrestline.example</div>
  </div>
  <div class="right">
    <div class="social"><span></span><span></span><span></span></div>
    <div class="sep"></div>
    <div class="item"><svg width="10" height="10" viewBox="0 0 20 20"><circle cx="10" cy="10" r="10" fill="#fff"/><text x="10" y="15" font-size="14" text-anchor="middle" fill="#174a9c" font-family="Lato" font-weight="700">?</text></svg>Do you have any questions?</div>
    <div class="quote">GET A FREE QUOTE</div>
  </div>
</div>

<header class="header">
  <div class="brand"><div class="mark"></div><div class="name">RV CRESTLINE ADVISORY</div></div>
  <nav class="nav">
    <a>HOME</a><a>ABOUT US</a><a>OUR SERVICES</a><a>WHY RV CRESTLINE</a><a>PARTNERS</a><a>CONTACT</a>
  </nav>
  <div class="search"><span><svg width="10" height="10" viewBox="0 0 20 20"><circle cx="8" cy="8" r="6" fill="none" stroke="#fff" stroke-width="2.5"/><path d="M12.5 12.5L18 18" stroke="#fff" stroke-width="2.5"/></svg></span></div>
</header>

<section class="hero">
  <div class="hero-photo" role="img" aria-label="Photo of business consultants working together at a laptop in a bright office"></div>
  <div class="hero-copy">
    <h1>SOLUTION THAT GIVES YOU</h1>
    <h2>MOVE FORWARD</h2>
    <p>RV Crestline Advisory is a U.S-based international consulting firm. We combined passion for success in the global business arena...</p>
    <div class="btns"><div class="btn solid">CONTACT US</div><div class="btn line">LEARN MORE</div></div>
  </div>
</section>

<h2 class="services-title">OUR SERVICE</h2>
<div class="rule"></div>
<p class="services-lead">le Lorem Ipsum n'est pas simplement du texte aléatoire. Il trouve ses racines dans une oeuvre de la littérature latine classique datant de 45 av. J.-C., le rendant vieux de 2000 ans.</p>

<div class="card c1 r1">
  <svg width="56" height="44" viewBox="0 0 56 44"><circle cx="20" cy="24" r="14" fill="none" stroke="#174a9c" stroke-width="7" stroke-dasharray="5 3"/><circle cx="20" cy="24" r="9" fill="#174a9c"/><circle cx="20" cy="24" r="4" fill="#fff"/><path d="M22 36L50 8l4 4-28 28-6 2z" fill="#174a9c" stroke="#fff" stroke-width="1.5"/></svg>
  <h3>IDENTIFYING AND DEVELOPING</h3>
  <p>It was popularised in the 1960s with the release of Kestrel sheets containing lorem</p>
  <div class="more">→ &nbsp;LEARN MORE</div>
</div>
<div class="card c2 r1">
  <svg width="46" height="44" viewBox="0 0 46 44"><rect x="2" y="22" width="7" height="20" fill="#174a9c"/><rect x="13" y="16" width="7" height="26" fill="#174a9c"/><rect x="24" y="24" width="7" height="18" fill="#174a9c"/><rect x="35" y="14" width="7" height="28" fill="#174a9c"/><path d="M2 18L14 8l10 10L40 3" fill="none" stroke="#174a9c" stroke-width="3"/><path d="M34 2h10v10z" fill="#174a9c"/></svg>
  <h3>ORGANIZING TRADE</h3>
  <p>Many desktop publishing packages and web page editors now use Lorem Ipsum</p>
  <div class="more">→ &nbsp;LEARN MORE</div>
</div>
<div class="card c3 r1">
  <svg width="44" height="52" viewBox="0 0 44 52" style="top:30px"><circle cx="22" cy="17" r="8" fill="#174a9c"/><rect x="19" y="24" width="6" height="5" fill="#174a9c"/><path d="M22 2v4M9 6l3 3M35 6l-3 3M5 17h4M35 17h4" stroke="#174a9c" stroke-width="2"/><path d="M4 50c0-10 6-16 18-16s18 6 18 16z" fill="#174a9c"/><path d="M22 35v12" stroke="#fff" stroke-width="2"/></svg>
  <h3 style="top:96px">SUCCESSFUL TRADE</h3>
  <p>Lorem Ipsum generators on the Internet tend to repeat predefined chunks as necessary.</p>
  <div class="more">→ &nbsp;LEARN MORE</div>
</div>

<div class="card c1 r2">
  <svg width="48" height="48" viewBox="0 0 48 48"><rect x="2" y="3" width="30" height="22" fill="none" stroke="#174a9c" stroke-width="3"/><path d="M9 20v-9M15 20v-6M21 20v-11" stroke="#174a9c" stroke-width="2.5"/><path d="M8 25l-4 20M26 25l4 20M17 25v20" stroke="#174a9c" stroke-width="3"/><circle cx="40" cy="15" r="4" fill="#174a9c"/><path d="M35 22h10v12h-2v12h-6V34h-2z" fill="#174a9c"/></svg>
  <h3>STRATEGIC EXPORT PLAN</h3>
  <p>Lorem Ipsum is that it has a more-or-less normal distribution of letters, as opposed</p>
  <div class="more">→ &nbsp;LEARN MORE</div>
</div>
<div class="card c2 r2">
  <svg width="48" height="48" viewBox="0 0 48 48"><rect x="8" y="4" width="14" height="10" fill="none" stroke="#174a9c" stroke-width="2.5"/><rect x="22" y="0" width="16" height="11" fill="none" stroke="#174a9c" stroke-width="2.5"/><circle cx="14" cy="26" r="4" fill="none" stroke="#174a9c" stroke-width="2.5"/><circle cx="34" cy="26" r="4" fill="none" stroke="#174a9c" stroke-width="2.5"/><path d="M3 46c0-8 5-12 11-12s11 4 11 12M23 46c0-8 5-12 11-12s11 4 11 12" fill="none" stroke="#174a9c" stroke-width="2.5"/></svg>
  <h3>ADDITIONAL RESOURCES</h3>
  <p>Combined with a handful of model sentence structures, to generate Lorem Ipsum</p>
  <div class="more">→ &nbsp;LEARN MORE</div>
</div>
<div class="card c3 r2">
  <svg width="52" height="54" viewBox="0 0 52 54"><circle cx="26" cy="8" r="5" fill="#174a9c"/><path d="M18 24c0-6 4-9 8-9s8 3 8 9z" fill="#174a9c"/><circle cx="10" cy="38" r="5" fill="#174a9c"/><path d="M2 54c0-6 4-9 8-9s8 3 8 9z" fill="#174a9c"/><circle cx="42" cy="38" r="5" fill="#174a9c"/><path d="M34 54c0-6 4-9 8-9s8 3 8 9z" fill="#174a9c"/><path d="M26 27v9M26 36l-9 7M26 36l9 7" stroke="#174a9c" stroke-width="2"/></svg>
  <h3 style="top:96px">CONNECTING COMPANIES</h3>
  <p>Lorem Ipsum used since the 1500s is reproduced below for those interested. Sections</p>
  <div class="more">→ &nbsp;LEARN MORE</div>
</div>

</body>
</html>
```